Enhance the web site presence of Kolrith Global Limited

Upgrade the current web site www.kolrithpanel.com to share with the audience our current plan and future developments of our company. I have created a worksheet which shows all the pages that I like to have. The home page in English, Japanese and Chinese is hyperlinked to the various pages. Under the product, we should allow the user to select "single sided PCB or double sided PCB". The translation of the contents of the pages with Japanese is not complete but the English and Chinese are complete. You can download the briefing and photos in the dropbox files below;

https://www.sharelocker.net/sh/xk4trw92mpd3ab1/BBQm_Lp841zzPq2Rw7KtYnHjEa?dl=0

Target Market(s)

Electronic companies

Industry/Entity Type

Electronic

Coding

Coded - Design and coding required

Number of Pages Required

5+ page

Font styles to use
Sans Serif

Colors
00a990
0353a1
33b8a4

Requirements
Must have
• Get a sense of confidence on our company's integrity and capability to deliver the highest quality PCBs with the most competitive prices and best services. A sense of elegance is essential as we DON'T treat profits as the number one goal. Our number goal is to do the RIGHT things right. Having a mixture of our company photos will be appropriate.

```html
<!DOCTYPE html>
<html lang="en">
<head>
<meta charset="utf-8">
<title>Kolrith Global Limited — Printed Circuit Boards</title>
<link rel="stylesheet" href="https://fonts.googleapis.com/css2?family=Bree+Serif&family=Open+Sans:wght@400;600;700&family=Roboto+Slab:wght@800&display=swap">
<style>
:root{
  --teal:#00a990;
  --teal-soft:#33b8a4;
  --mint:#7fdcc4;
  --mint-deep:#5ccdb0;
  --blue:#0353a1;
  --ink:#1f1f1f;
  --dark:#2b2b2b;
  --darker:#222;
  --white:#fff;
  --light:#f1f1f4;
}
*{box-sizing:border-box;margin:0;padding:0}
html,body{width:1200px;height:2639px;overflow:hidden}
body{font-family:"Open Sans",Arial,sans-serif;color:var(--ink);position:relative;background:var(--white)}

/* hero */
.hero{position:absolute;left:0;top:0;width:1200px;height:540px;
  background:linear-gradient(180deg,#3d4a44 0%,#56635c 40%,#3b4541 100%)}
.hero-photo{position:absolute;inset:0;background:
  radial-gradient(ellipse at 25% 70%,rgba(170,190,175,.55),transparent 55%),
  radial-gradient(ellipse at 80% 40%,rgba(120,150,130,.35),transparent 60%),
  linear-gradient(180deg,rgba(20,30,25,.35),rgba(20,30,25,.55))}
.brand{position:absolute;left:158px;top:20px;color:var(--teal-soft);font-family:"Bree Serif",serif;font-size:30px;letter-spacing:3px;line-height:1}
.brand-tag{position:absolute;left:158px;top:56px;color:var(--teal-soft);font-size:8px;font-weight:700;letter-spacing:.5px}
.topnav{position:absolute;right:158px;top:30px;display:flex;gap:26px;color:var(--white);font-family:"Bree Serif",serif;font-size:14px;align-items:center}
.topnav span{display:flex;align-items:center;gap:7px}
.wave{position:absolute;left:0;top:78px}
.hero-title{position:absolute;left:0;width:1200px;top:212px;text-align:center;color:var(--white);font-family:"Bree Serif",serif;font-weight:400;font-size:46px}
.hero-sub{position:absolute;left:0;width:1200px;top:284px;text-align:center;color:var(--white);font-size:14px;letter-spacing:.5px}
.btn{position:absolute;top:347px;height:40px;background:var(--teal);color:var(--white);font-family:"Bree Serif",serif;font-size:14px;display:flex;align-items:center;justify-content:center;letter-spacing:.5px}
.arrow{position:absolute;top:258px}

/* about */
.about{position:absolute;left:0;top:540px;width:1200px;height:757px;
  background:radial-gradient(ellipse at 50% 40%,#8fe4cd 0%,var(--mint) 45%,var(--mint-deep) 100%)}
.intro{position:absolute;left:158px;width:884px;top:80px;text-align:center;font-size:13px;line-height:18px;color:var(--ink)}
.intro p+p{margin-top:18px}
.feature-title{position:absolute;font-family:"Roboto Slab",serif;font-weight:800;font-size:22px;letter-spacing:1px;color:var(--ink);white-space:nowrap}
.feature-text{position:absolute;font-size:11.5px;line-height:18px;color:var(--ink)}
.more{position:absolute;font-size:11px;font-weight:700;letter-spacing:.3px}
.frame{position:absolute;background:rgba(40,170,140,.45);padding:12px}
.photo{width:100%;height:100%;background:linear-gradient(135deg,#3d9466,#e6eae4 55%,#9ea8a2)}

/* investment */
.invest{position:absolute;left:0;top:1297px;width:1200px;height:340px;
  background:linear-gradient(180deg,#2f3533,#4a5350 55%,#323836);color:var(--white);text-align:center}
.invest h2{position:absolute;left:0;width:1200px;top:82px;font-family:"Roboto Slab",serif;font-weight:800;font-size:21px;letter-spacing:1px}
.invest h3{position:absolute;left:0;width:1200px;top:160px;font-size:13.5px;font-weight:700}
.invest p{position:absolute;left:168px;width:864px;top:205px;font-size:11.5px;line-height:19px}

/* partners */
.partners{position:absolute;left:0;top:1637px;width:1200px;height:299px;background:linear-gradient(90deg,#ececec,#fafafa 50%,#e9e9e9)}
.partners h2{position:absolute;left:0;width:1200px;top:52px;text-align:center;font-family:"Roboto Slab",serif;font-weight:800;font-size:20px;letter-spacing:.3px;white-space:nowrap}
.card{position:absolute;top:123px;height:109px;background:var(--white);box-shadow:0 2px 8px rgba(0,0,0,.18);display:flex;align-items:center;justify-content:center}
.mark{border:2px solid #222;padding:10px 18px;font-size:21px;font-weight:600;color:var(--ink);display:flex;align-items:center;gap:10px}
.mark i{width:15px;height:15px;background:var(--blue);display:block}

/* contact */
.contact{position:absolute;left:0;top:1936px;width:1200px;height:261px;background:var(--light)}
.contact h2{position:absolute;left:0;width:1200px;top:44px;text-align:center;font-family:"Bree Serif",serif;font-weight:400;font-size:19px}
.rule{position:absolute;left:160px;width:878px;border-top:1px dashed #b8b8b8}
.field{position:absolute;top:146px;height:42px;background:var(--white);border:1px solid #dedede;font-size:11px;color:#999;padding:13px 14px}
.send{position:absolute;top:146px;left:961px;width:77px;height:42px;background:var(--teal);color:var(--white);font-weight:700;font-size:13px;display:flex;align-items:center;justify-content:center}

/* footer */
.footer{position:absolute;left:0;top:2197px;width:1200px;height:399px;background:var(--dark);color:#c8c8c8}
.footer .rule{border-color:#777}
.slogan{position:absolute;left:160px;top:64px;font-size:11px;color:#bbb;white-space:nowrap}
.slogan b{color:var(--teal-soft);font-family:"Bree Serif",serif;font-weight:400;font-size:15px;margin-right:6px}
.fcol h4{position:absolute;font-family:"Bree Serif",serif;font-weight:400;font-size:15px;color:var(--white)}
.fline{position:absolute;font-size:11px;line-height:18px;color:#b9b9b9}
.icon{position:absolute}
.navlist{position:absolute;left:931px;top:168px;font-size:11px;line-height:18px;color:#b9b9b9;list-style:none}
.bottom{position:absolute;left:0;top:2596px;width:1200px;height:43px;background:var(--darker);color:#8d8d8d;font-size:10px}
.bottom span{position:absolute;left:160px;top:15px}
.social{position:absolute;top:9px;width:24px;height:24px;background:#6a6a6a}
</style>
</head>
<body>

<section class="hero">
  <div class="hero-photo" role="img" aria-label="Photo of stacked green printed circuit board panels on the factory production line"></div>
  <div class="brand">Kolrith</div>
  <div class="brand-tag">Printed Circuit Boards Is Our Business</div>
  <nav class="topnav">
    <span><svg width="14" height="14" viewBox="0 0 14 14"><circle cx="6" cy="6" r="4.5" fill="none" stroke="#fff" stroke-width="2"/><path d="M9 9l4 4" stroke="#fff" stroke-width="2"/></svg>Search</span>
    <span><svg width="14" height="14" viewBox="0 0 14 14"><circle cx="7" cy="4" r="3.2" fill="#fff"/><path d="M1 14c0-4 3-6 6-6s6 2 6 6z" fill="#fff"/></svg>Sign In</span>
    <span><svg width="18" height="18" viewBox="0 0 18 18"><circle cx="9" cy="9" r="7.5" fill="none" stroke="#fff" stroke-width="1.4"/></svg>Language</span>
    <span>Menu <svg width="24" height="16" viewBox="0 0 24 16"><path d="M2 2h20M6 8h16M2 14h20" stroke="#fff" stroke-width="2"/></svg></span>
  </nav>
  <svg class="wave" width="1200" height="8" viewBox="0 0 1200 8"><line x1="0" y1="4" x2="1200" y2="4" stroke="#fff" stroke-width="1.4" stroke-dasharray="6 4"/></svg>
  <h1 class="hero-title">Specialized In Software Solution</h1>
  <div class="hero-sub">CONSULTING AND DATA INTEGRATION</div>
  <div class="btn" style="left:459px;width:113px">LEARN MORE</div>
  <div class="btn" style="left:604px;width:130px">CONTACT US</div>
  <svg class="arrow" style="left:52px" width="28" height="28" viewBox="0 0 28 28"><circle cx="14" cy="14" r="13" fill="rgba(0,0,0,.4)"/><path d="M16 8l-6 6 6 6" stroke="#fff" stroke-width="2.5" fill="none"/></svg>
  <svg class="arrow" style="left:1122px" width="28" height="28" viewBox="0 0 28 28"><circle cx="14" cy="14" r="13" fill="rgba(0,0,0,.4)"/><path d="M12 8l6 6-6 6" stroke="#fff" stroke-width="2.5" fill="none"/></svg>
</section>

<section class="about">
  <div class="intro">
    <p>Established in 2007, Kolrith Global Limited (Kolrith) is a Hong Kong company specializing in single and double sized printed circuit boards. Its manufacturing facility is located in a self-owned facility in Linhe, Dongguan of China which is 50 minutes from Hong Kong.<br>Our mission is to become a premium low costs PCB supplier that fully embraces human, social and environmental responsibilities.</p>
    <p>Through our insatiable drive to maximize efficiency, Kolrith is becoming a highly efficient PCB factory with a capacity of 140,000 square meter a month. PCB is our business and it is through continued automation and innovation that will drive our growth in the next 10 years.</p>
  </div>

  <h2 class="feature-title" style="left:161px;top:284px">SINGLE LAYERED PRINTED CIRCUIT BOARDS</h2>
  <div class="feature-text" style="left:161px;top:330px;width:540px">We are offering single layered circuit boards through our own production facility in China for customers in the following industries:<br><br>Our technical capability for the single sided PCB facility is (see the attached photo).</div>
  <div class="more" style="left:161px;top:424px">LEARN MORE</div>
  <div class="frame" style="left:757px;top:273px;width:281px;height:178px"><div class="photo" role="img" aria-label="Photo of single layered circuit board panels stacked beside production machinery"></div></div>

  <div class="frame" style="left:162px;top:488px;width:282px;height:181px"><div class="photo" role="img" aria-label="Photo of multi-layered circuit board panels stacked in the factory"></div></div>
  <h2 class="feature-title" style="right:162px;top:496px">MULTI-LAYERED PRINTED CIRCUIT BOARDS</h2>
  <div class="feature-text" style="right:162px;top:542px;width:550px;text-align:right">We are offering two layered and multi-layered circuit boards for our customers through our strategically approved printed circuit boards manufacturers.With our own UL for double sided and multi-Layered circuit boards, we work with a number of strategically approved manufacturers in delivering 100% quality guaranteed printed circuit boards for our customers.</div>
  <div class="more" style="right:162px;top:637px">LEARN MORE</div>
</section>

<section class="invest" role="img" aria-label="Background photo of the automated factory floor">
  <h2>OUR INVESTMENT AND UPGRADE</h2>
  <h3>MAINTAINING A HIGHLY AUTOMATED FACTORY IS THE ONLY WAY TO ENSURE CONSISTENT PRODUCT AND LONG TERM COMPETITIVE EFFICIENCY.</h3>
  <p>From 2015 to 2017, Kolrith invested over US$3.5 million in automating our production and quality control process and enhancing our environmental processing facility. We will spend a further US$1.5 million in 2018 to continue our improvement process to ensure we are one of the most efficient and highest quality single sided PCB manufacturers in Asia. By the end of 2018, 100% of our PCBs will be inspected by AVI before they are delivered to our customers.</p>
</section>

<section class="partners">
  <h2>KOLRITH IS EMBRACING A PHILOSOPHY OF BEING A PARTNER WITH OUR CUSTOMERS.</h2>
  <div class="card" style="left:160px;width:174px"><div class="mark">Norvane</div></div>
  <div class="card" style="left:363px;width:205px"><div class="mark"><i></i>Tekrio</div></div>
  <div class="card" style="left:600px;width:210px"><div class="mark"><i></i>Halvenko</div></div>
  <div class="card" style="left:841px;width:197px"><div class="mark">Brightmoor</div></div>
</section>

<section class="contact">
  <h2>Contact Form</h2>
  <div class="rule" style="top:99px"></div>
  <div class="field" style="left:160px;width:181px">Name</div>
  <div class="field" style="left:348px;width:231px">Email</div>
  <div class="field" style="left:588px;width:142px">Company Name</div>
  <div class="field" style="left:737px;width:215px">Message</div>
  <div class="send">SEND</div>
</section>

<footer class="footer">
  <div class="rule" style="top:47px"></div>
  <div class="slogan"><b>We are a young company with experience.</b>Specializing in single and double sized printed circuit boards. Its manufacturing facility is located in Linhe, China</div>
  <div class="rule" style="top:101px"></div>

  <div class="fcol">
    <h4 style="left:160px;top:133px">Hong Kong Address</h4>
    <svg class="icon" style="left:162px;top:170px" width="10" height="14" viewBox="0 0 10 14"><path d="M5 0a5 5 0 0 1 5 5c0 4-5 9-5 9S0 9 0 5a5 5 0 0 1 5-5z" fill="#33b8a4"/><circle cx="5" cy="5" r="2" fill="#2b2b2b"/></svg>
    <div class="fline" style="left:183px;top:166px">Kolrith Global Limited<br>28/F Harbour Crest 61 Marlow Road<br>Wanfield Bay, Hong Kong</div>
    <svg class="icon" style="left:160px;top:240px" width="14" height="12" viewBox="0 0 14 12"><path d="M1 4c3-4 9-4 12 0l-2 2-2-1V3H5v2L3 6z" fill="#33b8a4"/><rect x="3" y="7" width="8" height="5" fill="#33b8a4"/></svg>
    <div class="fline" style="left:183px;top:236px">Tel: +852-35550148<br>Fax: +852-35550192</div>
    <svg class="icon" style="left:160px;top:297px" width="14" height="10" viewBox="0 0 14 10"><rect width="14" height="10" fill="#33b8a4"/><path d="M0 0l7 6 7-6" stroke="#2b2b2b" fill="none"/></svg>
    <div class="fline" style="left:183px;top:292px">Email: sales@kolrithpanel.com</div>
  </div>

  <div class="fcol">
    <h4 style="left:477px;top:133px">Our China Address</h4>
    <svg class="icon" style="left:478px;top:170px" width="10" height="14" viewBox="0 0 10 14"><path d="M5 0a5 5 0 0 1 5 5c0 4-5 9-5 9S0 9 0 5a5 5 0 0 1 5-5z" fill="#33b8a4"/><circle cx="5" cy="5" r="2" fill="#2b2b2b"/></svg>
    <div class="fline" style="left:498px;top:166px">Kolrith Global (Dongguan) Limited<br>7 Qingshan East 4 Road,22 Industrial Park<br>Linhe Township, Dongguan<br>Guangdong Province, China 518420</div>
    <svg class="icon" style="left:476px;top:254px" width="14" height="12" viewBox="0 0 14 12"><path d="M1 4c3-4 9-4 12 0l-2 2-2-1V3H5v2L3 6z" fill="#33b8a4"/><rect x="3" y="7" width="8" height="5" fill="#33b8a4"/></svg>
    <div class="fline" style="left:498px;top:250px">Tel: +86-555<br>Fax: +86-555</div>
  </div>

  <div class="fcol">
    <h4 style="left:931px;top:133px">Navigation</h4>
    <ul class="navlist">
      <li>Home</li><li>Products</li><li>Our Facility</li><li>Customers</li><li>News</li><li>Quotes</li><li>Contact Us</li><li>Login</li>
    </ul>
  </div>
</footer>

<div class="bottom">
  <span>© 2018 Kolrith Global Limited,All Rights Reserved.</span>
  <div class="social" style="left:950px"></div>
  <div class="social" style="left:982px"></div>
  <div class="social" style="left:1014px"></div>
</div>

</body>
</html>
```